New Business Card Design Project

I have a logo I would like to use on the business card. I want something that will stand out and that will be remembered.

Target Market(s)

People who collect gems, minerals and crystals.

Contact Information for Business Card

email - mkthestonefalcon@vendrollo.com
phone # 917-406-2581

Font styles to use
Serif
Sans Serif
Decorative

Colors

Designer to choose colors to be used in the design.

Requirements
Must have
• The logo...two to choose from.
Nice to have
• An eye catching and memorable way to draw in people who collect gems minerals and crystals.

```html
<!DOCTYPE html>
<html lang="en">
<head>
<meta charset="utf-8">
<title>The Stone Falcon — Business Card</title>
<link href="https://fonts.googleapis.com/css2?family=Russo+One&family=Saira:wght@500;600&display=swap" rel="stylesheet">
<style>
  :root {
    --page: #3a3a3c;
    --card-dark: #161616;
    --card-light: #fbfbfb;
    --ink: #111111;
    --silver: #8a8a8a;
    --silver-soft: #5f5f5f;
    --royal: #0b1fbf;
    --mascot-dark: #2a2a2a;
    --mascot-light: #3b3b3b;
  }
  * { box-sizing: border-box; margin: 0; padding: 0; }
  html, body { width: 799px; height: 1200px; overflow: hidden; }
  body {
    background: var(--page);
    position: relative;
    font-family: "Russo One", sans-serif;
  }
  .card {
    position: absolute;
    left: 100px;
    width: 600px;
    height: 343px;
    overflow: hidden;
    box-shadow: 0 10px 24px rgba(0,0,0,.45);
  }
  /* front */
  .card--front { top: 150px; background: var(--card-dark); }
  .card--front .mascot {
    position: absolute; left: 60px; top: 90px;
    width: 150px; height: 160px; border-radius: 40px 40px 20px 20px;
    background: linear-gradient(160deg, var(--mascot-light), var(--mascot-dark));
  }
  .front-lockup {
    position: absolute; left: 235px; top: 128px;
    width: 335px;
  }
  .front-lockup .brand {
    font-size: 30px; line-height: 1; color: var(--silver);
    white-space: nowrap; letter-spacing: .5px;
  }
  .front-lockup .rule {
    margin: 14px 0 12px; height: 2px; background: var(--silver-soft);
  }
  .front-lockup .tagline {
    font-family: "Saira", sans-serif; font-weight: 500;
    font-size: 13px; line-height: 1; letter-spacing: 3.5px;
    color: var(--silver-soft); white-space: nowrap;
  }
  /* back */
  .card--back { top: 690px; background: var(--card-light); }
  .card--back .mascot {
    position: absolute; left: 45px; top: 70px;
    width: 120px; height: 130px; border-radius: 34px 34px 16px 16px;
    background: linear-gradient(160deg, #3a3a3a, #0f0f0f);
  }
  .contact { position: absolute; left: 195px; top: 90px; color: var(--ink); white-space: nowrap; }
  .contact__phone { font-size: 32px; line-height: 1; letter-spacing: .5px; }
  .contact__name {
    display: flex; align-items: center; gap: 10px;
    margin: 12px 0 10px; font-size: 16px; line-height: 1; color: var(--royal);
  }
  .contact__name::before, .contact__name::after {
    content: ""; width: 60px; height: 3px; background: var(--royal);
  }
  .contact__email { font-size: 17px; line-height: 1; letter-spacing: .3px; }
  .band { position: absolute; left: 0; bottom: 0; width: 600px; height: 150px; }
  .band__tagline {
    position: absolute; left: 40px; bottom: 40px;
    font-family: "Saira", sans-serif; font-weight: 600;
    font-size: 14px; letter-spacing: 4px; color: #fff; white-space: nowrap;
  }
</style>
</head>
<body>
  <section class="card card--front">
    <div class="mascot" role="img" aria-label="Brand mascot illustration holding crystals"></div>
    <div class="front-lockup">
      <div class="brand">THE STONE FALCON</div>
      <div class="rule"></div>
      <div class="tagline">GEMS · MINERALS · CRYSTALS</div>
    </div>
  </section>

  <section class="card card--back">
    <div class="mascot" role="img" aria-label="Brand mascot illustration holding crystals"></div>
    <div class="contact">
      <div class="contact__phone">CALL: 917-406-2581</div>
      <div class="contact__name">THE STONE FALCON</div>
      <div class="contact__email">MKTHESTONEFALCON@VENDROLLO.COM</div>
    </div>
    <svg class="band" viewBox="0 0 600 150" preserveAspectRatio="none" aria-hidden="true">
      <path d="M0 30 C 200 40, 420 80, 600 150 L0 150 Z" fill="var(--royal)"/>
    </svg>
    <div class="band__tagline">GEMS · MINERALS · CRYSTALS</div>
  </section>
</body>
</html>
```